Business Card Re-Design

Consulting Company: To build a high performance organization, you need great leaders at all levels throughout your organization. The Cedar Path Talent Institute engages, inspires, and educates current and future leaders to step beyond the ordinary and deliver exceptional results. This new breed of leaders will motivate your staff to leave the safety of complacency behind and come together to build an extraordinary organization. The current trend has been to ask our people to do more with fewer resources. People have been stepping up to the challenge, but more is required to ensure success with a new work paradigm. We work with your management team to build a successful strategy that will make your organization more effective. CPTI then supports your management team by providing a comprehensive set of proven services to empower your entire organization to successfully execute new strategies.Let CPTI help you optimize your organization’s individual and team performance today!

Target Market(s)

Federal, State and Local Government / Non profit

Industry/Entity Type

Management Consulting

Contact Information for Business Card

CPTI, inc (Cedar Path Talent Institute) Optimizing Individual and Organizational Performance

Colors
fee18a
ec1f27
474747
fbf289

Requirements
Must have
• Professional and high quality feel

```html
<!DOCTYPE html>
<html lang="en">
<head>
<meta charset="utf-8">
<title>Cedar Path Talent Institute – Business Card</title>
<link rel="stylesheet" href="https://fonts.googleapis.com/css2?family=Josefin+Sans:wght@400;600;700&family=Arimo:wght@400&display=swap">
<style>
  :root {
    --page-bg: #d9d6d2;
    --card-bg: #3b3b3b;
    --card-shade: #333333;
    --band-light: #f1efea;
    --ink-dark: #2f2f2f;
    --ink-light: #f2f0ec;
    --logo-ink: #dedad3;
    --figure-tone: #4a4a4a;
  }
  * { box-sizing: border-box; margin: 0; padding: 0; }
  html, body {
    width: 1200px; height: 800px; overflow: hidden;
    background: var(--page-bg);
  }
  .card {
    position: absolute; left: 150px; top: 143px;
    width: 900px; height: 514px;
    background: linear-gradient(135deg, var(--card-bg), var(--card-shade));
    box-shadow: 0 18px 40px rgba(0,0,0,.3);
    overflow: hidden;
  }
  .figures {
    position: absolute; left: 120px; top: 110px;
    width: 300px; height: 340px;
    border-radius: 120px 120px 20px 20px;
    background: radial-gradient(ellipse at center, var(--figure-tone) 0%, rgba(74,74,74,.5) 55%, rgba(59,59,59,0) 75%);
  }
  .brand {
    position: absolute; left: 150px; top: 200px; width: 270px;
    font-family: "Josefin Sans", sans-serif; font-weight: 700;
    color: var(--logo-ink); display: flex; align-items: center; gap: 14px;
  }
  .brand-dot {
    width: 22px; height: 22px; border-radius: 50%;
    background: var(--logo-ink); flex: none;
  }
  .brand-mark { font-size: 84px; line-height: .9; letter-spacing: 1px; }
  .brand-name {
    position: absolute; left: 150px; top: 290px; width: 290px;
    font-family: "Josefin Sans", sans-serif; font-weight: 700;
    color: var(--logo-ink); font-size: 15px; letter-spacing: 2px;
    text-transform: uppercase; line-height: 1.4;
  }
  .name-band {
    position: absolute; left: 470px; top: 95px; width: 430px; height: 100px;
    background: var(--band-light);
    padding: 22px 0 0 40px;
    font-family: "Josefin Sans", sans-serif; color: var(--ink-dark);
  }
  .person-name { font-size: 29px; font-weight: 700; letter-spacing: 5px; }
  .person-title {
    font-size: 11px; font-weight: 600; letter-spacing: 3px;
    margin: 6px 0 0 104px;
  }
  .contact-list { position: absolute; left: 470px; top: 230px; list-style: none; }
  .contact-item {
    position: relative; height: 55px;
    display: flex; align-items: center;
    font-family: "Arimo", sans-serif; color: var(--ink-light); font-size: 20px;
    letter-spacing: .5px; line-height: 1.3;
  }
  .contact-stripe {
    position: absolute; left: 0; top: 50%; width: 40px; height: 14px;
    margin-top: -7px; background: var(--band-light);
  }
  .contact-icon {
    position: absolute; left: 28px; top: 50%; margin-top: -17px;
    width: 34px; height: 34px; border-radius: 50%;
    background: var(--band-light);
    display: flex; align-items: center; justify-content: center;
  }
  .contact-text { margin-left: 90px; }
</style>
</head>
<body>
  <div class="card">
    <div class="figures" role="img" aria-label="Faint silhouettes of a group of people behind the brand name"></div>

    <div class="brand">
      <span class="brand-dot"></span>
      <span class="brand-mark">CPTI</span>
    </div>
    <div class="brand-name">Cedar Path Talent<br>Institute, inc</div>

    <div class="name-band">
      <div class="person-name">MARCUS L. REEVE</div>
      <div class="person-title">PRESIDENT / CEO</div>
    </div>

    <ul class="contact-list">
      <li class="contact-item">
        <span class="contact-stripe"></span>
        <span class="contact-icon">
          <svg width="18" height="18" viewBox="0 0 24 24" fill="#3b3b3b"><path d="M6.6 10.8a15 15 0 0 0 6.6 6.6l2.2-2.2c.3-.3.7-.4 1-.2 1.1.4 2.3.6 3.6.6.6 0 1 .4 1 1V20c0 .6-.4 1-1 1A17 17 0 0 1 3 4c0-.6.4-1 1-1h3.5c.6 0 1 .4 1 1 0 1.3.2 2.5.6 3.6.1.3 0 .7-.2 1z"/></svg>
        </span>
        <span class="contact-text">555.014.2281</span>
      </li>
      <li class="contact-item">
        <span class="contact-stripe"></span>
        <span class="contact-icon">
          <svg width="18" height="18" viewBox="0 0 24 24" fill="#3b3b3b"><path d="M6 2h12v5H6zM4 8h16a2 2 0 0 1 2 2v7h-4v5H6v-5H2v-7a2 2 0 0 1 2-2zm4 8v4h8v-4z"/></svg>
        </span>
        <span class="contact-text">555.014.2297</span>
      </li>
      <li class="contact-item">
        <span class="contact-stripe"></span>
        <span class="contact-icon">
          <svg width="18" height="18" viewBox="0 0 24 24" fill="none" stroke="#3b3b3b" stroke-width="2.2"><rect x="3" y="5" width="18" height="14"/><path d="M3 5l9 8 9-8"/></svg>
        </span>
        <span class="contact-text">mreeve@cedarpath.example</span>
      </li>
      <li class="contact-item">
        <span class="contact-stripe"></span>
        <span class="contact-icon">
          <svg width="18" height="18" viewBox="0 0 24 24" fill="#3b3b3b"><path d="M12 3l10 9h-3v9h-5v-6h-4v6H5v-9H2z"/></svg>
        </span>
        <span class="contact-text">742 Willow Ridge Lane<br>Fairbrook, MD 20999</span>
      </li>
    </ul>
  </div>
</body>
</html>
```